Halvex Consulting

Hi,
I have my own network consulting business (just me)
and need to get a logo and business card design together,

Based in New Zealand,

Gareth Pollard
Unified Communications and Network Architect

/design engineer,
and would like this to be the basis for personal branding and company identity

Reason: I will be off site for a couple of days - so you have some more time

Business

• I have the basis for a optional logo - needs color -

```html
<!DOCTYPE html>
<html lang="en">
<head>
<meta charset="utf-8">
<title>Halvex Consulting – Business Card</title>
<link href="https://fonts.googleapis.com/css2?family=Titillium+Web:ital,wght@0,400;0,700;1,700&display=swap" rel="stylesheet">
<style>
  :root {
    --page-bg: #5a5a5a;
    --card-deep: #04304f;
    --card-mid: #0a4a78;
    --card-glow: #2f7fb6;
    --text-white: #ffffff;
    --name-blue: #7fd0f5;
    --accent-black: #000000;
    --mark-blue: #4fb3ea;
  }
  * { margin: 0; padding: 0; box-sizing: border-box; }
  html, body {
    width: 1200px;
    height: 800px;
    overflow: hidden;
    background: var(--page-bg);
    font-family: "Titillium Web", sans-serif;
  }
  .canvas {
    width: 1200px;
    height: 800px;
    display: flex;
    align-items: center;
    justify-content: center;
  }
  .business-card {
    position: relative;
    width: 1050px;
    height: 600px;
    overflow: hidden;
    background:
      radial-gradient(ellipse 520px 380px at 80% 26%, var(--card-glow) 0%, var(--card-mid) 45%, transparent 100%),
      linear-gradient(160deg, var(--card-mid) 0%, var(--card-deep) 100%);
    color: var(--text-white);
  }
  .brand {
    position: absolute;
    left: 300px;
    top: 96px;
    display: flex;
    align-items: center;
    gap: 40px;
  }
  .brand-name {
    font-size: 52px;
    font-weight: 700;
    color: var(--text-white);
    line-height: 1;
  }
  .brand-dot {
    width: 76px;
    height: 76px;
    border-radius: 50%;
    background: var(--mark-blue);
  }
  .accent-bar {
    position: absolute;
    left: 0;
    top: 372px;
    width: 52px;
    height: 160px;
    background: var(--accent-black);
  }
  .contact {
    position: absolute;
    left: 73px;
    top: 388px;
    line-height: 1.2;
  }
  .contact-name {
    font-size: 34px;
    font-weight: 400;
    color: var(--name-blue);
    letter-spacing: 0.5px;
    margin-bottom: 2px;
  }
  .contact-role,
  .contact-line {
    font-size: 25px;
    font-weight: 400;
  }
  .contact-title {
    font-size: 27px;
    font-weight: 700;
    font-style: italic;
  }
</style>
</head>
<body>
  <main class="canvas">
    <section class="business-card">
      <div class="brand">
        <span class="brand-name">Halvex Consulting</span>
        <span class="brand-dot" aria-hidden="true"></span>
      </div>

      <div class="accent-bar"></div>

      <div class="contact">
        <p class="contact-name">Gareth Pollard</p>
        <p class="contact-role">Unified Communications and Network Architect</p>
        <p class="contact-title">design engineer</p>
        <p class="contact-line">mobile: (+00)mobile number</p>
        <p class="contact-line">email: youremail@domain.com</p>
      </div>
    </section>
  </main>
</body>
</html>
```